Sales presentation for Veltro-7

Veltro-7.com is a digital intelligence service which provides news and analysis about digital business models and ecosystems. The readers are C-Suite executives such as chief executive officers, chief marketing officers, chief information officers, strategists, company directors and internet entrepreneurs.

.

Target Market(s)

The audience for the presentation are strategy managers and media buyers at advertising agencies and marketing managers of technology companies and professional service companies.

Industry/Entity Type

Sales

Requirements
Must have
• Slides 9 and 10 have rough diagrams that need to be professionally designed.
Nice to have
• Slide 12 could do with a better piece of generic art

```html
<!DOCTYPE html>
<html lang="en">
<head>
<meta charset="utf-8">
<title>Calverin Model — Veltro-7</title>
<link rel="stylesheet" href="https://fonts.googleapis.com/css2?family=League+Gothic&family=Quicksand:wght@500&display=swap">
<style>
  :root {
    --paper: #dedede;
    --ink: #26215e;
    --segment-deep: #78abd9;
    --segment-light: #a6c7e4;
    --hub: #103a5c;
    --label: #1d2433;
    --white: #ffffff;
  }
  * { margin: 0; padding: 0; box-sizing: border-box; }
  html, body {
    width: 1200px;
    height: 675px;
    overflow: hidden;
    background: var(--paper);
  }
  .slide {
    position: relative;
    width: 1200px;
    height: 675px;
    background: var(--paper);
    overflow: hidden;
  }
  .slide-title {
    position: absolute;
    left: 47px;
    top: 22px;
    font-family: "League Gothic", "Arial Narrow", sans-serif;
    font-weight: 400;
    font-size: 112px;
    line-height: 1;
    letter-spacing: 1px;
    color: var(--ink);
  }
  .model-wheel {
    position: absolute;
    left: 47px;
    top: 148px;
    width: 460px;
    height: 460px;
  }
  .segment { stroke: var(--paper); stroke-width: 7; }
  .segment--deep { fill: var(--segment-deep); }
  .segment--light { fill: var(--segment-light); }
  .segment-label {
    font-family: "Quicksand", "Helvetica", sans-serif;
    font-weight: 500;
    font-size: 17.5px;
    fill: var(--label);
    text-anchor: middle;
  }
  .hub { fill: var(--hub); }
  .hub-label {
    font-family: "Quicksand", "Helvetica", sans-serif;
    font-weight: 500;
    font-size: 18px;
    fill: var(--white);
    text-anchor: middle;
  }
  .points { list-style: none; }
  .point {
    position: absolute;
    right: 98px;
    width: 600px;
    text-align: right;
    font-family: "League Gothic", "Arial Narrow", sans-serif;
    font-size: 26px;
    line-height: 33px;
    letter-spacing: 0.4px;
    color: var(--ink);
  }
  .point::after {
    content: "";
    position: absolute;
    right: -66px;
    top: var(--dot-top);
    width: 28px;
    height: 28px;
    border-radius: 50%;
    background: var(--ink);
  }
  .point--one { top: 184px; --dot-top: 19px; }
  .point--two { top: 281px; --dot-top: 12px; }
  .point--three { top: 376px; --dot-top: 36px; }
  .point--four { top: 502px; --dot-top: 2px; }
</style>
</head>
<body>
<main class="slide">
  <h1 class="slide-title">CALVERIN MODEL</h1>

  <svg class="model-wheel" viewBox="-230 -230 460 460" aria-label="Calverin model wheel with the customer at the centre">
    <path class="segment segment--deep"  d="M-158.4,-158.4 A224,224 0 0 1 0,-224 L0,-84 A84,84 0 0 0 -59.4,-59.4 Z"/>
    <path class="segment segment--light" d="M0,-224 A224,224 0 0 1 158.4,-158.4 L59.4,-59.4 A84,84 0 0 0 0,-84 Z"/>
    <path class="segment segment--deep"  d="M158.4,-158.4 A224,224 0 0 1 224,0 L84,0 A84,84 0 0 0 59.4,-59.4 Z"/>
    <path class="segment segment--light" d="M224,0 A224,224 0 0 1 158.4,158.4 L59.4,59.4 A84,84 0 0 0 84,0 Z"/>
    <path class="segment segment--deep"  d="M158.4,158.4 A224,224 0 0 1 0,224 L0,84 A84,84 0 0 0 59.4,59.4 Z"/>
    <path class="segment segment--light" d="M0,224 A224,224 0 0 1 -158.4,158.4 L-59.4,59.4 A84,84 0 0 0 0,84 Z"/>
    <path class="segment segment--deep"  d="M-158.4,158.4 A224,224 0 0 1 -224,0 L-84,0 A84,84 0 0 0 -59.4,59.4 Z"/>
    <path class="segment segment--light" d="M-224,0 A224,224 0 0 1 -158.4,-158.4 L-59.4,-59.4 A84,84 0 0 0 -84,0 Z"/>

    <text class="segment-label" x="-64" y="-154">Advertising</text>
    <text class="segment-label" x="64" y="-154">News</text>
    <text class="segment-label" x="144" y="-52">Features</text>
    <text class="segment-label" x="145" y="60">Opinion</text>
    <text class="segment-label" x="64" y="134">Guest</text>
    <text class="segment-label" x="64" y="162">Columns</text>
    <text class="segment-label" x="-61" y="134">Special</text>
    <text class="segment-label" x="-61" y="162">Reports</text>
    <text class="segment-label" x="-143" y="46">Custom</text>
    <text class="segment-label" x="-143" y="74">Publishing</text>
    <text class="segment-label" x="-145" y="-52">Advertorial</text>

    <circle class="hub" r="62"/>
    <text class="hub-label" y="6">CUSTOMER</text>
  </svg>

  <ul class="points">
    <li class="point point--one">The Calverin model turns the traditional model around on itself<br>putting the customer at the centre of the conversation.</li>
    <li class="point point--two">The model recognises that customers want to apply their own<br>filters to content</li>
    <li class="point point--three">By editorialising your content marketing we amplify your story<br>to our readers in a way that engages their interest, matches<br>their workflow and promote share-ability</li>
    <li class="point point--four">In the Calverin model customers determine the value of content</li>
  </ul>
</main>
</body>
</html>
```